Export company based in South America (Ecuador) we export flowers, chocolate, and bananas

We need a website that gives our potential clients and introduction into our company and the different types of commodities we export around the world. We are based in Quito, Ecuador so the website should portray the feel of Ecuadorian landscapes within a modern looking website.
At the moment we are exporting roses, chocolate, and bananas so the website should have an intro to our company and then three different areas that describe our three main commodity. The three different sections should explain why each of the products from Ecuador are some of the best in the world in their categories and the benefits of importing the commodity through our company.
Industry/Entity Type
Commodity
Number of Pages Required
4 page

```html
<!DOCTYPE html>
<html lang="en">
<head>
<meta charset="utf-8">
<title>Andesta — We Export Around The World</title>
<link href="https://fonts.googleapis.com/css2?family=Fjalla+One&family=Montserrat:wght@400;500;600&display=swap" rel="stylesheet">
<style>
:root{
  --ink:#1c1c1c;
  --dark:#232323;
  --navy:#1b3d5f;
  --yellow:#f5d35a;
  --yellow-deep:#f1c94a;
  --white:#ffffff;
  --text:#2b2b2b;
  --muted:#4a4a4a;
  --line-light:rgba(255,255,255,.25);
  --head:"Fjalla One",sans-serif;
  --body:"Montserrat",sans-serif;
}
*{margin:0;padding:0;box-sizing:border-box}
html,body{width:1200px;height:3475px;overflow:hidden}
body{position:relative;font-family:var(--body);color:var(--text);background:var(--navy)}
.abs{position:absolute}
h1,h2,h3{font-family:var(--head);font-weight:400}

/* header */
.site-header{left:0;top:0;width:1200px;height:96px;background:var(--dark)}
.brand{display:flex;align-items:center;gap:10px;color:var(--white);font-family:var(--body);font-weight:600;font-size:28px;letter-spacing:.5px}
.brand-dot{width:36px;height:36px;border-radius:50%;background:var(--white);display:inline-block}
.site-header .brand{left:74px;top:28px}
.main-nav{left:615px;top:38px;display:flex;gap:24px;font-size:13px;color:var(--white)}
.main-nav a{color:inherit;text-decoration:none}
.main-nav a.active{color:var(--yellow)}
.search-icon{left:964px;top:35px}
.btn{font-family:var(--head);letter-spacing:1.5px;display:flex;align-items:center;justify-content:center;font-size:16px;box-shadow:3px 3px 0 var(--white)}
.btn-quote{left:1007px;top:30px;width:116px;height:35px;background:var(--yellow);color:var(--ink)}

/* hero */
.hero{left:0;top:96px;width:1200px;height:592px;background:radial-gradient(ellipse at 60% 50%,#5b4332 0%,#3b2a1f 50%,#241912 100%)}
.hero-hand{left:0;top:96px;width:560px;height:592px;background:linear-gradient(120deg,#d9d9d9 0%,#b99c86 35%,rgba(150,110,85,0) 85%)}
.hero-eyebrow{left:0;top:244px;width:1200px;text-align:center;font-size:27px;color:var(--yellow)}
.hero-title{left:0;top:284px;width:1200px;text-align:center;font-size:82px;color:var(--white);line-height:1}
.hero-text{left:300px;top:406px;width:600px;text-align:center;color:var(--white);font-size:13px;line-height:24px}
.dots{left:521px;top:583px;display:flex;gap:61px}
.dots span{width:11px;height:11px;border-radius:50%;background:var(--white)}
.dots span.off{background:transparent;border:2px solid var(--white)}

/* about */
.about-card{left:150px;top:631px;width:899px;height:558px;background:var(--yellow);box-shadow:0 6px 18px rgba(0,0,0,.25);text-align:center}
.about-card h2{margin-top:82px;font-size:68px;color:var(--ink);line-height:1}
.about-text{width:580px;margin:38px auto 0;font-size:12.5px;line-height:24px;color:var(--text)}
.btn-explore{left:389px;top:426px;width:118px;height:36px;background:var(--navy);color:var(--white)}

/* features */
.feature{top:1278px;width:260px;color:var(--white)}
.feature-icon{width:81px;height:81px;border:1.5px solid var(--white);border-radius:50%;display:flex;align-items:center;justify-content:center}
.feature h3{position:absolute;left:95px;top:38px;font-size:35px;line-height:1}
.feature p{margin-top:33px;width:215px;font-size:11px;line-height:22px}
.divider-v{width:1px;background:var(--line-light)}

/* products */
.products{left:0;top:1540px;width:1200px;height:590px;background:var(--white)}
.products-title{left:150px;top:1660px;font-size:66px;color:var(--ink);line-height:1}
.products-text{left:150px;top:1768px;width:338px;font-size:12.5px;line-height:24px;color:var(--text)}
.btn-show{left:150px;top:1957px;width:116px;height:38px;background:var(--yellow);color:var(--ink);box-shadow:3px 3px 0 var(--yellow-deep),4px 4px 0 var(--white)}
.product-card{top:1661px;width:287px;height:347px;background:var(--white);box-shadow:0 6px 16px rgba(0,0,0,.12);text-align:center}
.product-photo{height:160px}
.product-card h3{margin-top:30px;font-size:34px;color:var(--ink);line-height:1}
.product-card p{width:214px;margin:16px auto 0;font-size:11px;line-height:22px;color:var(--muted)}
.photo-roses{background:linear-gradient(135deg,#c4282a,#7b1a1f 50%,#d23a33)}
.photo-chocolate{background:radial-gradient(ellipse at 55% 55%,#a5685a 0%,#7c5a3f 45%,#3a2c20 100%)}
.photo-bananas{background:linear-gradient(135deg,#8b7a36,#4d4322)}

/* benefits */
.port-photo{left:0;top:2231px;width:616px;height:516px;background:linear-gradient(160deg,#a7a095 0%,#3a6f8e 40%,#2b5f80 70%,#3c7a96 100%)}
.benefits-card{left:333px;top:2321px;width:716px;height:609px;background:var(--yellow)}
.benefits-title{left:74px;top:80px;font-size:66px;color:var(--ink);line-height:1}
.benefits-lead{left:322px;top:88px;width:335px;font-size:12.5px;line-height:24px;color:var(--text)}
.benefit{width:240px}
.benefit svg{position:absolute;left:0;top:0}
.benefit h3{margin-left:50px;font-size:25px;color:var(--ink);line-height:1;padding-top:6px}
.benefit p{margin:16px 0 0 50px;width:170px;font-size:11px;line-height:22px;color:var(--muted)}
.benefits-line-v{left:372px;top:247px;width:1px;height:303px;background:rgba(0,0,0,.15)}
.benefits-line-h{left:86px;top:399px;width:539px;height:1px;background:rgba(0,0,0,.15)}

/* newsletter */
.newsletter-title{left:0;top:3040px;width:1200px;text-align:center;font-size:90px;color:var(--white);line-height:1}
.newsletter-text{left:0;top:3162px;width:1200px;text-align:center;font-size:13px;color:var(--white)}
.newsletter-form{left:384px;top:3228px;width:430px;height:54px;background:var(--white)}
.newsletter-form span{position:absolute;left:16px;top:19px;font-size:13px;color:#9a9a9a}
.btn-subscribe{left:305px;top:7px;width:116px;height:38px;background:var(--yellow);color:var(--ink);box-shadow:3px 3px 0 var(--yellow-deep)}

/* footer */
.site-footer{left:0;top:3404px;width:1200px;height:71px;background:var(--dark)}
.site-footer .brand{left:74px;top:20px;font-size:23px}
.site-footer .brand-dot{width:30px;height:30px}
.copyright{left:0;top:28px;width:1200px;text-align:center;font-size:12.5px;color:var(--white)}
.socials{left:982px;top:23px;display:flex;gap:15px}
.socials span{width:24px;height:24px;border-radius:50%;background:#3f6fb5}
.socials span.pink{background:#c43a8e}
.socials span.sky{background:#3ea3e8}
.socials span.blue{background:#1473b4}
</style>
</head>
<body>

<header class="site-header abs">
  <div class="brand abs"><span class="brand-dot"></span>Andesta</div>
  <nav class="main-nav abs">
    <a class="active" href="#">Home</a><a href="#">About</a><a href="#">Services</a><a href="#">Blogs</a><a href="#">Contact Us</a>
  </nav>
  <svg class="search-icon abs" width="24" height="24" viewBox="0 0 24 24" fill="none" stroke="#fff" stroke-width="2.4"><circle cx="10" cy="10" r="7.5"/><line x1="15.5" y1="15.5" x2="22" y2="22"/></svg>
  <div class="btn btn-quote abs">Get A Quote</div>
</header>

<section class="hero abs" role="img" aria-label="Hands holding a pile of cocoa beans"></section>
<div class="hero-hand abs" role="img" aria-label="Cupped hand and shirt sleeve"></div>
<p class="hero-eyebrow abs">We Export</p>
<h1 class="hero-title abs">Around The World</h1>
<p class="hero-text abs">Lorem Ipsum Is Simply Dummy Text Of The Printing And Typesetting Industry. Lorem Ipsum Has<br>Been The Industry's Standard Dummy Text Ever Since The 1500s, When</p>
<div class="dots abs"><span class="off"></span><span></span><span></span></div>

<section class="about-card abs">
  <h2>About Us</h2>
  <p class="about-text">Lorem Ipsum Is Simply Dummy Text Of The Printing And Typesetting Industry. Lorem Ipsum Has Been The Industry's Standard Dummy Text Ever Since The 1500s, When An Unknown Printer Took A Galley Of Type And Scrambled It To Make A Type Specimen Book. It Has Survived Not Only Five Centuries, But Also<br>The Leap Into Electronic Typesetting, Remaining Essentially Unchanged. It Was Popularised In The 1960s With The Release Of Typeset Sheets Containing Lorem Ipsum Passages, And More Recently With Desktop Publishing Software Like Folio Layout Including Versions Of Lorem Ipsum.</p>
  <div class="btn btn-explore abs">Explore More</div>
</section>

<div class="feature abs" style="left:150px">
  <div class="feature-icon"><svg width="40" height="40" viewBox="0 0 40 40" fill="none" stroke="#f5d35a" stroke-width="1.5"><circle cx="20" cy="17" r="12"/><circle cx="20" cy="17" r="8"/><path d="M20 12l1.6 3.3 3.6.5-2.6 2.5.6 3.6-3.2-1.7-3.2 1.7.6-3.6-2.6-2.5 3.6-.5z"/><path d="M13 27l-3 9 5-2 3 4 2-7M27 27l3 9-5-2-3 4-2-7"/></svg></div>
  <h3>Quality</h3>
  <p>Lorem Ipsum Is Simply Dummy Text Of The Printing And Typesetting Industry. Lorem Ipsum</p>
</div>
<div class="divider-v abs" style="left:426px;top:1278px;height:171px"></div>
<div class="feature abs" style="left:492px">
  <div class="feature-icon"><svg width="42" height="42" viewBox="0 0 42 42" fill="none" stroke="#f5d35a" stroke-width="1.5"><circle cx="23" cy="24" r="13"/><circle cx="23" cy="24" r="9"/><path d="M19 8h8M23 8v3M19 21l3 4 6-6M4 20h6M2 25h7M5 30h6"/></svg></div>
  <h3>Quickness</h3>
  <p>Lorem Ipsum Is Simply Dummy Text Of The Printing And Typesetting Industry. Lorem Ipsum</p>
</div>
<div class="divider-v abs" style="left:776px;top:1278px;height:171px"></div>
<div class="feature abs" style="left:840px">
  <div class="feature-icon"><svg width="40" height="40" viewBox="0 0 40 40" fill="none" stroke="#f5d35a" stroke-width="1.5"><rect x="7" y="5" width="24" height="30" rx="2"/><path d="M12 12h14M12 17h14M12 22h7M12 27h5"/><circle cx="27" cy="27" r="5"/><path d="M31 31l4 4"/></svg></div>
  <h3>Result</h3>
  <p>Lorem Ipsum Is Simply Dummy Text Of The Printing And Typesetting Industry. Lorem Ipsum</p>
</div>

<section class="products abs"></section>
<h2 class="products-title abs">Our Products</h2>
<p class="products-text abs">Lorem Ipsum Is Simply Dummy Text Of The Printing And Typesetting Industry. Lorem Ipsum Has Been The Industry's Standard Dummy Text Ever Since The 1500s, When An Unknown Printer Took A Galley Of Type And Scrambled It To Make A Type Specimen Book. It Has Survived Not Only Five Centuries,</p>
<div class="btn btn-show abs">Show All</div>

<article class="product-card abs" style="left:554px">
  <div class="product-photo photo-roses" role="img" aria-label="Boxes of red roses packed for export"></div>
  <h3>Roses</h3>
  <p>Lorem Ipsum Is Simply Dummy Text Of The Printing And Typesetting Industry. Lorem Ipsum</p>
</article>
<article class="product-card abs" style="left:860px">
  <div class="product-photo photo-chocolate" role="img" aria-label="Sack of cocoa beans with a scoop"></div>
  <h3>Chocolate</h3>
  <p>Lorem Ipsum Is Simply Dummy Text Of The Printing And Typesetting Industry. Lorem Ipsum</p>
</article>
<article class="product-card abs" style="left:1166px">
  <div class="product-photo photo-bananas" role="img" aria-label="Bunches of bananas"></div>
</article>

<div class="port-photo abs" role="img" aria-label="Aerial view of a cargo ship being loaded by port cranes"></div>
<section class="benefits-card abs">
  <h2 class="benefits-title abs">Benefits</h2>
  <p class="benefits-lead abs">Lorem Ipsum Dolor Sit Amet, Consectetur Adipiscing Elit, Sed Do Eiusmod Tempor Incididunt Ut Labore Et Dolore Magna Aliqua. Ut Enim Ad Minim Veniam, Quis Nostrud Exercitation Ullamco</p>
  <div class="benefits-line-v abs"></div>
  <div class="benefits-line-h abs"></div>

  <div class="benefit abs" style="left:89px;top:267px">
    <svg width="36" height="40" viewBox="0 0 36 40" fill="none" stroke="#1c1c1c" stroke-width="1.6"><path d="M18 2l14 5v11c0 10-6 16-14 20C10 34 4 28 4 18V7z"/><circle cx="18" cy="19" r="8"/><path d="M14 19l3 3 5-6"/></svg>
    <h3>Safe Ingredients</h3>
    <p>Lorem Ipsum Dolor Sit Amet, Consectetur Adipiscing Elit,</p>
  </div>
  <div class="benefit abs" style="left:407px;top:267px">
    <svg width="40" height="40" viewBox="0 0 40 40" fill="none" stroke="#1c1c1c" stroke-width="1.6"><path d="M20 22V8M20 14c-4-4-9-2-9-2s2 6 9 4M20 12c4-4 9-2 9-2s-2 6-9 4"/><path d="M2 30h8l6 2h8c2 0 2 3 0 3H14M24 33l10-5c2-1 4 1 2 3l-12 6H2"/></svg>
    <h3>Eco Friendly</h3>
    <p>Lorem Ipsum Dolor Sit Amet, Consectetur Adipiscing Elit,</p>
  </div>
  <div class="benefit abs" style="left:89px;top:432px">
    <svg width="36" height="40" viewBox="0 0 36 40" fill="none" stroke="#1c1c1c" stroke-width="1.6"><path d="M5 2h18l8 8v28H5z"/><path d="M23 2v8h8"/><rect x="10" y="16" width="5" height="5"/><rect x="10" y="26" width="5" height="5"/><path d="M19 18h8M19 21h6M19 28h8M19 31h6"/></svg>
    <h3>100% Tested</h3>
    <p>Lorem Ipsum Dolor Sit Amet, Consectetur Adipiscing Elit,</p>
  </div>
  <div class="benefit abs" style="left:407px;top:432px">
    <svg width="40" height="40" viewBox="0 0 40 40" fill="none" stroke="#1c1c1c" stroke-width="1.6"><circle cx="20" cy="20" r="4"/><path d="M20 16c-3-5-1-12 0-12s3 7 0 12M24 20c5-3 12-1 12 0s-7 3-12 0M20 24c3 5 1 12 0 12s-3-7 0-12M16 20c-5 3-12 1-12 0s7-3 12 0"/></svg>
    <h3>Natural Based</h3>
    <p>Lorem Ipsum Dolor Sit Amet, Consectetur Adipiscing Elit,</p>
  </div>
</section>

<h2 class="newsletter-title abs">Subscribe To Our Newsletter</h2>
<p class="newsletter-text abs">Continually Productize Business Scenarios Through Transparent Niches. Synergistically Impact Web-Enabled</p>
<form class="newsletter-form abs">
  <span>Email</span>
  <div class="btn btn-subscribe abs">Subscribe</div>
</form>

<footer class="site-footer abs">
  <div class="brand abs"><span class="brand-dot"></span>Andesta</div>
  <p class="copyright abs">Copyright © ,2020 All Right Reserved</p>
  <div class="socials abs"><span></span><span class="sky"></span><span class="pink"></span><span class="blue"></span></div>
</footer>

</body>
</html>
```